Educational Agency in Abu Dhabi looking for an 8 pages website

We are looking for an 8 pages design for a website, we already have one but we need to refine it and it is www.korvalendi.ae - Please base it on logo colours (attached) I have uploaded our logo, website content logo colors to use it for the scheme.
We are looking for a smooth look and content added if possible, I also attached content and logo

Industry/Entity Type

Education

Coding

Coded - Design and coding required

Number of Pages Required

5+ page

```html
<!DOCTYPE html>
<html lang="en">
<head>
<meta charset="utf-8">
<title>Korvalendi — Study Abroad</title>
<link href="https://fonts.googleapis.com/css2?family=Roboto:wght@300;400;500;700&display=swap" rel="stylesheet">
<style>
:root{
  --pink:#ff3668;
  --navy:#1f3367;
  --ink:#2b2f36;
  --muted:#b3b7bd;
  --panel:#f0f3f4;
  --white:#ffffff;
  --tile-red:#ef5263;
  --tile-blue:#4356b0;
  --tile-sky:#3f7de0;
  --tile-dark:#3f444e;
}
*{box-sizing:border-box;margin:0;padding:0}
html,body{width:1200px;height:1200px;overflow:hidden;background:var(--white);font-family:'Roboto',sans-serif;color:var(--ink)}
.page{position:relative;width:1200px;height:1200px}
.site-header{position:absolute;left:0;top:0;width:1200px;height:84px}
.brand{position:absolute;left:66px;top:0;width:112px;height:108px;background:var(--white);z-index:3;display:flex;flex-direction:column;align-items:center;justify-content:center;gap:6px}
.brand-mark{width:14px;height:14px;background:var(--navy)}
.brand-name{font-weight:700;font-size:15px;color:var(--navy);letter-spacing:.5px}
.phone{position:absolute;left:822px;top:30px;font-size:17px;font-weight:300;color:var(--muted);letter-spacing:.5px}
.apply-top{position:absolute;left:996px;top:0;width:84px;height:84px;background:var(--pink);color:var(--white);font-size:14px;text-align:center;line-height:16px;display:flex;align-items:center;justify-content:center}
.menu-btn{position:absolute;left:1080px;top:0;width:84px;height:84px;background:var(--navy)}
.menu-btn span{position:absolute;left:26px;width:32px;height:2px;background:var(--white)}
.hero{position:absolute;left:36px;top:84px;width:1128px;height:434px;overflow:hidden}
.hero-photo{position:absolute;inset:0;background:linear-gradient(90deg,#3a3534 0%,#6b4f45 35%,#a88a78 60%,#c9c0b8 80%,#8e8a86 100%)}
.hero-shade{position:absolute;inset:0;background:linear-gradient(90deg,rgba(20,18,20,.55) 0%,rgba(20,18,20,.25) 55%,rgba(0,0,0,0) 80%)}
.hero-copy{position:absolute;left:78px;top:100px;width:590px;color:var(--white)}
.hero-copy h1{font-size:32px;font-weight:700;line-height:40px}
.hero-copy p{margin-top:24px;font-size:14.5px;line-height:24px;font-weight:400}
.hero-actions{position:absolute;left:78px;top:306px;display:flex;gap:16px}
.btn{width:174px;height:48px;border-radius:2px;font-size:15px;font-weight:500;display:flex;align-items:center;justify-content:center}
.btn-primary{background:var(--pink);color:var(--white)}
.btn-light{background:#eef1f3;color:var(--pink);width:171px}
.partners-band{position:absolute;left:36px;top:518px;width:1128px;height:153px;background:var(--panel)}
.section-title{position:absolute;left:0;width:1200px;text-align:center;font-size:24px;font-weight:500;color:var(--ink)}
.section-title span{display:inline-block;padding-bottom:4px;border-bottom:3px solid var(--pink)}
.partners{position:absolute;left:82px;top:627px;display:flex;gap:15px}
.partner{width:160px;height:88px;background:var(--white);box-shadow:0 2px 6px rgba(0,0,0,.08);display:flex;align-items:center;gap:10px;padding-left:18px}
.partner-badge{width:40px;height:50px;border-radius:4px 4px 20px 20px;background:#c9cbce;flex:none}
.partner-name{font-size:13px;line-height:15px;color:#9a9da1}
.destinations{position:absolute;left:36px;top:826px;display:grid;grid-template-columns:repeat(4,264px);column-gap:24px;row-gap:24px}
.destination{height:182px;background:var(--white);box-shadow:0 1px 8px rgba(0,0,0,.07);display:flex;flex-direction:column;align-items:center;padding-top:40px;border:1px solid transparent}
.destination.is-active{border-color:var(--pink);box-shadow:none}
.destination-tile{width:110px;height:74px;border-radius:8px}
.destination-label{margin-top:18px;font-size:18px;color:var(--ink)}
</style>
</head>
<body>
<div class="page">
  <header class="site-header">
    <div class="brand"><div class="brand-mark"></div><div class="brand-name">KORVALENDI</div></div>
    <div class="phone">+971 2 480 17 36</div>
    <div class="apply-top">APPLY<br>NOW</div>
    <div class="menu-btn"><span style="top:32px"></span><span style="top:41px"></span><span style="top:50px"></span></div>
  </header>

  <section class="hero">
    <div class="hero-photo" role="img" aria-label="Photo of smiling students with a backpack and laptop on campus"></div>
    <div class="hero-shade"></div>
    <div class="hero-copy">
      <h1>Korvalendi is the number one<br>choice for students to study abroad</h1>
      <p>KORVALENDI Abu Dhabi, one of the leading and fastest growing educational consulting company based in UAE officially recognized by Ministry of Higher Education and Scientific Research, GEAC Agency and ISO9001.</p>
    </div>
    <div class="hero-actions">
      <div class="btn btn-primary">Why study abroad?</div>
      <div class="btn btn-light">Apply now</div>
    </div>
  </section>

  <div class="partners-band"></div>
  <h2 class="section-title" style="top:558px"><span>Our Partners</span></h2>
  <div class="partners">
    <div class="partner"><div class="partner-badge"></div><div class="partner-name">Halbrook<br>University</div></div>
    <div class="partner"><div class="partner-badge"></div><div class="partner-name">Halbrook<br>University</div></div>
    <div class="partner"><div class="partner-badge"></div><div class="partner-name">Halbrook<br>University</div></div>
    <div class="partner"><div class="partner-badge"></div><div class="partner-name">Halbrook<br>University</div></div>
    <div class="partner"><div class="partner-badge"></div><div class="partner-name">Halbrook<br>University</div></div>
    <div class="partner"><div class="partner-badge"></div><div class="partner-name">Halbrook<br>University</div></div>
  </div>

  <h2 class="section-title" style="top:756px"><span>Study Destinations</span></h2>
  <div class="destinations">
    <div class="destination">
      <div class="destination-tile" role="img" aria-label="Flag of the United Kingdom" style="background:linear-gradient(135deg,var(--tile-blue),var(--tile-red))"></div>
      <div class="destination-label">Study in UK</div>
    </div>
    <div class="destination is-active">
      <div class="destination-tile" role="img" aria-label="Flag of the United States" style="background:linear-gradient(135deg,var(--tile-sky),var(--tile-red))"></div>
      <div class="destination-label">Study in USA</div>
    </div>
    <div class="destination">
      <div class="destination-tile" role="img" aria-label="Flag of Australia" style="background:linear-gradient(135deg,var(--tile-blue),#5b6cc2)"></div>
      <div class="destination-label">Study in Australia</div>
    </div>
    <div class="destination">
      <div class="destination-tile" role="img" aria-label="Flag of New Zealand" style="background:linear-gradient(135deg,#3a4ca6,var(--tile-blue))"></div>
      <div class="destination-label">Study in New Zealand</div>
    </div>
    <div class="destination">
      <div class="destination-tile" role="img" aria-label="Flag of the European Union" style="background:var(--tile-sky)"></div>
      <div class="destination-label">Study in Europe</div>
    </div>
    <div class="destination">
      <div class="destination-tile" role="img" aria-label="Flag of Malaysia" style="background:linear-gradient(135deg,var(--tile-blue),var(--tile-red))"></div>
      <div class="destination-label">Study in Malaysia</div>
    </div>
    <div class="destination">
      <div class="destination-tile" role="img" aria-label="Flag of China" style="background:var(--tile-red)"></div>
      <div class="destination-label">Study in China</div>
    </div>
    <div class="destination">
      <div class="destination-tile" role="img" aria-label="Flag of Germany" style="background:linear-gradient(180deg,var(--tile-dark),var(--tile-red),#f6c03f)"></div>
      <div class="destination-label">Study in Germany</div>
    </div>
  </div>
</div>
</body>
</html>
```